Contact card for an aggressive entrepreneur

I am looking for a business/contact card as an individual. I operate under the company name The Varden Collective, LLC (but don't generally use that other than for billing). I have explored a few ideas and am now turning to artplaza to connect with people more creative than me. I am trying to capture a diverse set of passions, which I will summarize with the following keywords (which may or may not be ON the card and are in no particular order):

entrepreneur
shark diver
MBA
visionary
defenseman
marketing guru
hockey coach
teacher
reader
writer
cook
captain
scuba diver
beach bum
Type A
Brightwater
Vermont
New York
Montauk
founder
leader
focused
driven
teammate father

hope that makes some sense!
Updates

Please note the photo is for reference - unless there is a really creative way to use it I do not need a card with a head shot (I am not a model or an actor!)

Project Deadline Extended
Reason: There have been several requests to submit designs so we will close this project this Wednesday and select a design by this Friday. Thank you to all for your great ideas and submissions!

I am reviewing the designs and will select one by end of day tomorrow, Tuesday, EST
Thank you to all who participated!

Target Market(s)

everyone from business contacts to personal acquaintances

Industry/Entity Type

Business

Requirements
Must have
• Must be utterly original, extraordinary and memorable.
How it achieves that is up to you!
Essential contact information that needs to be included:

phone: (555) 374-1926
email: tomas@vardencollective.example
skype: tomas.varden
Nice to have
• A striking visual whether that is a photo or illustration
Some way of conveying the diversity of what I am and what I do
Feel free to use the printing or physical material of the card to make it stand out.
Should not have
• I am not into "logos" but that being said I do not want to limit creativity in any way so feel free to ignore any part of this brief if you disagree with me. No need to use the attached photo of me, but that's what I look like.

```html
<!DOCTYPE html>
<html lang="en">
<head>
<meta charset="utf-8">
<title>Tomas Varden — Contact Card</title>
<link rel="stylesheet" href="https://fonts.googleapis.com/css2?family=Jost:wght@400;500&family=Ubuntu:wght@400;700&display=swap">
<style>
  :root {
    --backdrop: #3a2417;
    --card-white: #ffffff;
    --taupe: #9b9784;
    --taupe-word: #b9b6a5;
    --word-highlight: #ffffff;
    --ink: #1c1c1c;
    --accent-green: #2fae3c;
    --rule-green: #6cc574;
  }
  * { box-sizing: border-box; margin: 0; padding: 0; }
  html, body {
    width: 1200px;
    height: 800px;
    overflow: hidden;
  }
  body {
    position: relative;
    background: var(--backdrop);
  }

  /* Front: contact side */
  .card-front {
    position: absolute;
    left: 175px;
    top: 125px;
    width: 420px;
    height: 420px;
    background: var(--card-white);
    font-family: "Ubuntu", sans-serif;
  }
  .name-band {
    position: absolute;
    left: 100px;
    right: 0;
    top: 100px;
    height: 64px;
    background: var(--taupe);
    display: flex;
    align-items: center;
    padding-left: 12px;
  }
  .name-band h1 {
    color: var(--card-white);
    font-weight: 700;
    font-size: 19px;
    letter-spacing: 1px;
    text-transform: uppercase;
  }
  .contact-list {
    position: absolute;
    left: 0;
    right: 8px;
    top: 196px;
    border-top: 1px solid var(--rule-green);
    list-style: none;
  }
  .contact-row {
    display: flex;
    align-items: stretch;
    height: 40px;
    border-bottom: 1px solid var(--rule-green);
  }
  .contact-label {
    width: 100px;
    padding-right: 8px;
    text-align: right;
    color: var(--accent-green);
    font-size: 14px;
    align-self: flex-end;
    padding-bottom: 5px;
  }
  .contact-value {
    flex: 1;
    border-left: 1px solid var(--rule-green);
    padding-left: 9px;
    display: flex;
    align-items: center;
    color: var(--ink);
    font-size: 18px;
    letter-spacing: -0.2px;
    white-space: nowrap;
  }

  /* Back: word cloud side */
  .card-back {
    position: absolute;
    left: 625px;
    top: 265px;
    width: 405px;
    height: 405px;
    background: var(--taupe);
    font-family: "Jost", sans-serif;
    text-transform: uppercase;
    color: var(--taupe-word);
    padding: 20px 26px 20px 30px;
  }
  .word-cloud {
    height: 100%;
    display: flex;
    flex-direction: column;
    justify-content: space-between;
  }
  .word-line {
    display: flex;
    justify-content: space-between;
    align-items: baseline;
    white-space: nowrap;
    line-height: 1;
    letter-spacing: 1px;
  }
  .word-line .lead {
    color: var(--word-highlight);
    letter-spacing: 3px;
  }
</style>
</head>
<body>

  <section class="card-front" aria-label="Contact side">
    <div class="name-band"><h1>Tomas Varden</h1></div>
    <ul class="contact-list">
      <li class="contact-row"><span class="contact-label">phone</span><span class="contact-value">555.374.1926</span></li>
      <li class="contact-row"><span class="contact-label">email</span><span class="contact-value">tomas@vardencollective.example</span></li>
      <li class="contact-row"><span class="contact-label">skype</span><span class="contact-value">tomas.varden</span></li>
    </ul>
  </section>

  <section class="card-back" aria-label="Passions side">
    <div class="word-cloud">
      <p class="word-line"><span style="font-size:24px">Trail Hiker</span><span style="font-size:30px">Sailor</span></p>
      <p class="word-line"><span style="font-size:18px">Night Owl</span><span style="font-size:28px">Climber</span></p>
      <p class="word-line"><span class="lead" style="font-size:44px">Builder</span></p>
      <p class="word-line"><span style="font-size:26px">Free Diver</span><span style="font-size:20px">Baker</span></p>
      <p class="word-line"><span style="font-size:32px">Strategist</span></p>
      <p class="word-line"><span style="font-size:20px">Maine</span><span style="font-size:30px">Boston</span></p>
      <p class="word-line"><span style="font-size:22px">Nantucket</span><span style="font-size:26px">Mentor</span></p>
      <p class="word-line"><span style="font-size:28px">Curious</span><span style="font-size:30px">Bold</span></p>
      <p class="word-line"><span style="font-size:20px">Organizer</span><span style="font-size:22px">Partner</span><span style="font-size:16px">Friend</span></p>
      <p class="word-line"><span style="font-size:26px">Storyteller</span><span style="font-size:20px">Uncle</span></p>
    </div>
  </section>

</body>
</html>
```